Corporate Identity Design for Travel Company

We need a brand book, that should include the following artwork:

Business card
Letterhead
Envelope (DL, C4, C5)
A4 folder
A4 paper for notes
E-mail signature
Power point template
Pen design

Please, submit your designs that include business card, letterhead and envelope. Once selected the winner, he will be asked to complete the project by creating the rest of the artwork.

Logo and project requirements are attached.

```html
<!DOCTYPE html>
<html lang="en">
<head>
<meta charset="utf-8">
<title>Northway Travel – Business Card</title>
<link href="https://fonts.googleapis.com/css2?family=Philosopher:wght@400;700&display=swap" rel="stylesheet">
<style>
  :root {
    --backdrop: #d9dbda;
    --card-dark: #5f6661;
    --card-dark-deep: #474d49;
    --card-light: #ffffff;
    --card-light-shade: #eceeed;
    --band-grey: #646b66;
    --band-black: #262727;
    --ink: #3a3d3b;
    --ink-soft: #e8ece9;
    --brand-square: #8fc84a;
  }
  * { box-sizing: border-box; margin: 0; padding: 0; }
  html, body { width: 1200px; height: 900px; overflow: hidden; }
  body {
    background: var(--backdrop);
    font-family: "Philosopher", Georgia, serif;
    position: relative;
  }
  .card {
    position: absolute;
    left: 250px;
    width: 700px;
    height: 400px;
    overflow: hidden;
    box-shadow: 0 6px 18px rgba(0,0,0,0.18);
  }

  /* Front */
  .card--front {
    top: 40px;
    background: linear-gradient(160deg, var(--card-dark) 0%, var(--card-dark-deep) 100%);
  }
  .card--front .texture {
    position: absolute;
    left: 0; right: 0; bottom: 0;
    height: 60%;
    background: linear-gradient(180deg, rgba(255,255,255,0) 0%, rgba(255,255,255,0.07) 55%, rgba(255,255,255,0.02) 100%);
  }
  .brand {
    position: absolute;
    top: 118px;
    left: 420px;
    display: flex;
    align-items: center;
    gap: 14px;
  }
  .brand__mark {
    width: 40px; height: 40px;
    background: var(--brand-square);
    border-radius: 6px;
  }
  .brand__name {
    color: var(--ink-soft);
    font-size: 30px;
    line-height: 1.0;
    font-weight: 400;
    letter-spacing: 0.5px;
  }
  .website {
    position: absolute;
    left: 60px;
    bottom: 72px;
    color: var(--ink-soft);
    font-size: 14px;
    letter-spacing: 0.6px;
  }

  /* Back */
  .card--back {
    top: 470px;
    background: linear-gradient(180deg, var(--card-light-shade) 0%, var(--card-light) 55%);
  }
  .card--back .texture {
    position: absolute;
    left: 260px; right: 0; top: 0;
    height: 65%;
    background: radial-gradient(ellipse at 60% 35%, rgba(120,128,122,0.12) 0%, rgba(120,128,122,0) 70%);
  }
  .nameplate {
    position: absolute;
    left: 0;
    top: 228px;
  }
  .nameplate__name {
    display: block;
    width: 300px;
    background: var(--band-grey);
    color: #ffffff;
    font-size: 22px;
    font-weight: 700;
    line-height: 1.3;
    padding: 3px 20px 3px 56px;
  }
  .nameplate__title {
    display: block;
    width: 220px;
    background: var(--band-black);
    color: #ffffff;
    font-size: 15px;
    line-height: 1.3;
    padding: 3px 20px 3px 62px;
  }
  .divider {
    position: absolute;
    left: 378px;
    top: 128px;
    width: 2px;
    height: 84px;
    background: linear-gradient(180deg, rgba(0,0,0,0) 0%, rgba(0,0,0,0.2) 50%, rgba(0,0,0,0) 100%);
  }
  .contact {
    position: absolute;
    left: 398px;
    top: 128px;
    color: var(--ink);
    font-size: 14px;
    line-height: 1.5;
    list-style: none;
  }
  .contact li { display: flex; align-items: center; gap: 5px; white-space: nowrap; }
  .contact svg { width: 13px; height: 13px; fill: var(--ink); flex: none; }
  .contact .gap { margin-left: 6px; }
</style>
</head>
<body>

<section class="card card--front" aria-label="Business card front">
  <div class="texture" role="img" aria-label="Subtle pattern of rounded squares"></div>
  <div class="brand">
    <span class="brand__mark"></span>
    <span class="brand__name">Northway<br>Travel</span>
  </div>
  <p class="website">www.northwaytravel.com</p>
</section>

<section class="card card--back" aria-label="Business card back">
  <div class="texture" role="img" aria-label="Faint pattern of rounded squares"></div>
  <div class="nameplate">
    <span class="nameplate__name">Daniel Hart</span>
    <span class="nameplate__title">President</span>
  </div>
  <div class="divider"></div>
  <ul class="contact">
    <li>123, Your Street, Your City, Country, 123.</li>
    <li>
      <svg viewBox="0 0 16 16"><path d="M1 6c0-2 3-3 7-3s7 1 7 3v1h-3V6H4v1H1z M4 8h8l2 5H2z"/></svg>262-555-0148
      <svg class="gap" viewBox="0 0 16 16"><path d="M1 6c0-2 3-3 7-3s7 1 7 3v1h-3V6H4v1H1z M4 8h8l2 5H2z"/></svg>877-555-0192
    </li>
    <li>
      <svg viewBox="0 0 16 16"><path d="M1 3h14v10H1z M2 4.5v.3l6 4 6-4v-.3z" fill-rule="evenodd"/></svg>hart@northwaytravel.com
    </li>
  </ul>
</section>

</body>
</html>
```